Maple Hollow Grain Farm

We need a business card with some pizam in it. Our slogan is something different so something a little different would do!

Industry/Entity Type

Business

```html
<!DOCTYPE html>
<html lang="en">
<head>
<meta charset="utf-8">
<title>Maple Hollow Grain Farm – Business Card</title>
<link href="https://fonts.googleapis.com/css2?family=Quicksand:wght@500;600;700&display=swap" rel="stylesheet">
<style>
  :root {
    --olive: #5e632a;
    --olive-soft: #8a8f4a;
    --card: #f6f6f6;
    --ink: #111111;
    --page: #ffffff;
    --shadow: rgba(0, 0, 0, 0.28);
  }
  html, body {
    margin: 0;
    padding: 0;
    width: 1200px;
    height: 1000px;
    overflow: hidden;
    background: var(--page);
    font-family: "Quicksand", sans-serif;
  }
  .canvas {
    position: relative;
    width: 1200px;
    height: 1000px;
  }
  .card {
    position: absolute;
    left: 282px;
    width: 693px;
    height: 406px;
    background: var(--card);
    box-shadow: 1px 2px 4px var(--shadow);
    overflow: hidden;
  }
  .card--front { top: 72px; }
  .card--back { top: 529px; }
  .tab {
    position: absolute;
    left: 202px;
    width: 289px;
    height: 50px;
    background: var(--olive);
  }
  .tab--top { top: 0; border-radius: 0 0 24px 24px; }
  .tab--bottom { bottom: 0; border-radius: 24px 24px 0 0; }

  /* Wordmark lockup: plain circle, rules, name */
  .lockup {
    position: absolute;
    display: flex;
    flex-direction: column;
    align-items: center;
    color: var(--olive);
  }
  .lockup__dot {
    border-radius: 50%;
    background: var(--olive);
  }
  .lockup__rule {
    border: 0;
    margin: 0;
    border-top: 3px solid var(--olive);
    border-bottom: 1px solid var(--olive-soft);
  }
  .lockup__name {
    margin: 0;
    font-weight: 700;
    line-height: 1.02;
    text-align: center;
    text-transform: uppercase;
  }

  .card--front .lockup {
    left: 158px;
    top: 86px;
    width: 378px;
  }
  .card--front .lockup__dot { width: 40px; height: 40px; margin-bottom: 14px; }
  .card--front .lockup__rule { width: 340px; height: 4px; }
  .card--front .lockup__name {
    font-size: 50px;
    letter-spacing: 2px;
    padding: 12px 0 10px;
  }

  .card--back .lockup {
    left: 400px;
    top: 140px;
    width: 232px;
  }
  .card--back .lockup__dot { width: 24px; height: 24px; margin-bottom: 8px; }
  .card--back .lockup__rule { width: 210px; height: 3px; border-top-width: 2px; }
  .card--back .lockup__name {
    font-size: 30px;
    letter-spacing: 1px;
    padding: 7px 0 6px;
  }

  .contact-name {
    position: absolute;
    left: 68px;
    top: 110px;
    margin: 0;
    font-size: 26px;
    font-weight: 700;
    color: var(--ink);
  }
  .contact-title {
    position: absolute;
    left: 68px;
    top: 142px;
    margin: 0;
    font-size: 19px;
    font-weight: 700;
    color: var(--ink);
  }
  .contact-list {
    position: absolute;
    left: 62px;
    top: 181px;
    margin: 0;
    padding: 0;
    list-style: none;
  }
  .contact-list li {
    display: flex;
    align-items: center;
    height: 31.5px;
    font-size: 20px;
    font-weight: 500;
    color: var(--ink);
  }
  .contact-icon {
    width: 30px;
    height: 26px;
    margin-right: 24px;
    flex: none;
  }
</style>
</head>
<body>
<main class="canvas">
  <section class="card card--front" aria-label="Card front">
    <div class="tab tab--top"></div>
    <div class="lockup">
      <span class="lockup__dot"></span>
      <hr class="lockup__rule">
      <p class="lockup__name">Maple Hollow<br>Grain Farm</p>
      <hr class="lockup__rule">
    </div>
    <div class="tab tab--bottom"></div>
  </section>

  <section class="card card--back" aria-label="Card back">
    <div class="tab tab--top"></div>
    <h1 class="contact-name">Your Name here</h1>
    <p class="contact-title">Your Title Here</p>
    <ul class="contact-list">
      <li>
        <svg class="contact-icon" viewBox="0 0 28 24" aria-hidden="true">
          <rect x="9" y="2" width="10" height="19" rx="1.5" fill="none" stroke="#111" stroke-width="1.8"/>
          <line x1="12.5" y1="18" x2="15.5" y2="18" stroke="#111" stroke-width="1.6"/>
        </svg>
        000.000.0000
      </li>
      <li>
        <svg class="contact-icon" viewBox="0 0 28 24" aria-hidden="true">
          <path d="M9 3c-2 1-3 3-2 6 1.5 4 4.5 8 8.5 11 2 1.5 4 1 5-.5l-3-3-2.5 1.5c-2-1.5-4-4-5-6.5L12 9.5 9 3z" fill="#111"/>
        </svg>
        000.000.0000
      </li>
      <li>
        <svg class="contact-icon" viewBox="0 0 28 24" aria-hidden="true">
          <circle cx="14" cy="12" r="11.5" fill="#111"/>
          <g fill="none" stroke="#f6f6f6" stroke-width="1.2">
            <ellipse cx="14" cy="12" rx="5" ry="11.5"/>
            <line x1="2.5" y1="12" x2="25.5" y2="12"/>
            <path d="M4.5 6.5h19M4.5 17.5h19"/>
          </g>
        </svg>
        www.maplehollowgrain.com
      </li>
      <li>
        <svg class="contact-icon" viewBox="0 0 28 24" aria-hidden="true">
          <rect x="3" y="5" width="22" height="14" fill="none" stroke="#111" stroke-width="1.6"/>
          <path d="M3 5l11 8 11-8M3 19l8-7M25 19l-8-7" fill="none" stroke="#111" stroke-width="1.4"/>
        </svg>
        youremail@mailbox.com
      </li>
    </ul>
    <div class="lockup">
      <span class="lockup__dot"></span>
      <hr class="lockup__rule">
      <p class="lockup__name">Maple Hollow<br>Grain Farm</p>
      <hr class="lockup__rule">
    </div>
    <div class="tab tab--bottom"></div>
  </section>
</main>
</body>
</html>
```